CalmPeak Nurses' Manifesto

Design a manifesto to inspire and motivate nurses to work at minimum standards of excellence in their nursing practice.

The manifesto will become a feature of our website, at conferences, workshops and retreats. It will also be featured on other marketing tools.

Primary Market:
Nurses and/or other healthcare professionals (specifically Doctors, Occupational Therapists, Psychologists and Social Workers).

However the manifesto is equally applicable to all nurses and healthcare professionals from new graduates to very experienced senior clinicians, administration officers,managers and healthcare executive personnel.

Mainly females and primarily 35 to 65 years old, which suggests people in this target age group have extensive experience, but have become jaded'.

The purpose of our business is to assist healthcare professionals, primarily nurses, to maintain their enthusiasm and excellence in service provision, for their benefit as well as the benefit of the clients.

I have attached:
File 1: Copy Samples and examples: which has the copy for the manifesto, examples that appeal to us and our 3 attempts.
File 2: Our colour Spec Sheet, HOWEVER the colours are not necessary limited to these colours. These colours are not in the logo that will be on the manifesto. The colours on the logo attached can/or also be used.
File 3: Prototype logo. The final logo will be available within 3 to 4 days.

Industry/Entity Type

Healthcare

Requirements
Must have
• Must use the copy as per the attached file.

It should be contemporary, eye catching and motivational.

Should not have
• MUST BE EASY TO READ. Each line MUST be clearly defined from each other.

```html
<!DOCTYPE html>
<html lang="en">
<head>
<meta charset="utf-8">
<title>CalmPeak – A Nurses' Manifesto</title>
<link href="https://fonts.googleapis.com/css2?family=Alfa+Slab+One&display=swap" rel="stylesheet">
<style>
  :root {
    --teal: #5ec3c4;
    --slate: #76748e;
    --ink: #1b1a1a;
    --orange: #f2892c;
    --cream-light: #fffdf3;
    --cream-edge: #fbe9bf;
    --slab: "Alfa Slab One", Georgia, serif;
  }
  html, body { margin: 0; padding: 0; overflow: hidden; }
  body { width: 849px; height: 1200px; }
  .manifesto {
    display: block;
    width: 849px;
    height: 1200px;
    background: radial-gradient(ellipse at 50% 45%, var(--cream-light) 40%, var(--cream-edge) 100%);
  }
  .manifesto text { font-family: var(--slab); font-weight: 400; }
  .teal { fill: var(--teal); }
  .slate { fill: var(--slate); }
  .ink { fill: var(--ink); }
  .orange { fill: var(--orange); }
  .dream { filter: drop-shadow(0 0 4px rgba(94,195,196,.7)); }
  .brand-mark { fill: var(--teal); }
</style>
</head>
<body>
<svg class="manifesto" width="849" height="1200" viewBox="0 0 849 1200" xmlns="http://www.w3.org/2000/svg" lang="en">
  <g class="heading">
    <text class="ink" x="383" y="75" font-size="40" textLength="417" lengthAdjust="spacingAndGlyphs">A Nurses' Manifesto</text>
  </g>

  <g class="block-nurse">
    <text class="teal" x="45" y="165" font-size="105" textLength="323" lengthAdjust="spacingAndGlyphs">NURSE</text>
    <text class="ink" x="47" y="200" font-size="24" textLength="175" lengthAdjust="spacingAndGlyphs">WITH OPEN</text>
    <text class="ink" x="228" y="200" font-size="38" textLength="134" lengthAdjust="spacingAndGlyphs">HANDS,</text>
    <text class="ink" x="46" y="238" font-size="38" textLength="149" lengthAdjust="spacingAndGlyphs">HEARTS</text>
    <text class="ink" x="203" y="238" font-size="24" textLength="17" lengthAdjust="spacingAndGlyphs">&amp;</text>
    <text class="ink" x="228" y="238" font-size="38" textLength="140" lengthAdjust="spacingAndGlyphs">MINDS</text>
  </g>

  <g class="block-self">
    <text class="slate" x="388" y="113" font-size="27" textLength="164" lengthAdjust="spacingAndGlyphs">LOOK AFTER</text>
    <text class="slate" x="388" y="170" font-size="62" textLength="252" lengthAdjust="spacingAndGlyphs">YOURSELF</text>
    <text class="slate" x="656" y="170" font-size="28" textLength="116" lengthAdjust="spacingAndGlyphs">&amp; VALUE</text>
    <text class="slate" x="388" y="207" font-size="30" textLength="404" lengthAdjust="spacingAndGlyphs">YOUR HEALTH AS MUCH AS YOU</text>
    <text class="slate" x="388" y="240" font-size="30" textLength="415" lengthAdjust="spacingAndGlyphs">VALUE THE HEALTH OF OTHERS.</text>
  </g>

  <g class="block-delight">
    <text class="orange" x="46" y="273" font-size="20" textLength="256" lengthAdjust="spacingAndGlyphs">DELIGHT YOUR CLIENTS &amp;</text>
    <text class="orange" x="46" y="296" font-size="20" textLength="370" lengthAdjust="spacingAndGlyphs">COLLEAGUES BY EXCEEDING THEIR</text>
    <text class="orange" x="425" y="298" font-size="62" textLength="375" lengthAdjust="spacingAndGlyphs">EXPECTATIONS</text>
  </g>

  <text class="ink" x="46" y="344" font-size="50" textLength="757" lengthAdjust="spacingAndGlyphs">DELIVER CARE SKILLFULLY.</text>

  <g class="block-respect">
    <text class="slate" x="46" y="396" font-size="46" textLength="219" lengthAdjust="spacingAndGlyphs">RESPECT</text>
    <text class="slate" x="275" y="396" font-size="18" textLength="129" lengthAdjust="spacingAndGlyphs">THE LIMITS OF</text>
    <text class="slate" x="46" y="416" font-size="18" textLength="359" lengthAdjust="spacingAndGlyphs">PEOPLE'S KNOWLEDGE &amp; SHARE YOUR</text>
    <text class="slate" x="46" y="436" font-size="18" textLength="250" lengthAdjust="spacingAndGlyphs">KNOWLEDGE GENEROUSLY.</text>
  </g>

  <g class="block-support">
    <text class="orange" x="433" y="404" font-size="53" textLength="174" lengthAdjust="spacingAndGlyphs">SUPPORT</text>
    <text class="orange" x="620" y="382" font-size="22" textLength="180" lengthAdjust="spacingAndGlyphs">YOUR COLLEAGUES</text>
    <text class="orange" x="433" y="432" font-size="22" textLength="179" lengthAdjust="spacingAndGlyphs">&amp; CHAMPION THEIR</text>
    <text class="orange" x="620" y="432" font-size="50" textLength="183" lengthAdjust="spacingAndGlyphs">PURPOSE.</text>
  </g>

  <g class="block-learn">
    <text class="ink" x="46" y="478" font-size="42" textLength="757" lengthAdjust="spacingAndGlyphs">LEARN SOMETHING NEW EACH DAY.</text>
    <text class="slate" x="46" y="499" font-size="16" textLength="754" lengthAdjust="spacingAndGlyphs">TRUST YOUR KNOWLEDGE &amp; SEEK ADVICE ONLY FROM RESPECTED SOURCES.</text>
    <text class="orange" x="46" y="550" font-size="52" textLength="757" lengthAdjust="spacingAndGlyphs">BE A LIFELONG LEARNER.</text>
  </g>

  <g class="block-diversity">
    <text class="ink" x="46" y="600" font-size="50" textLength="757" lengthAdjust="spacingAndGlyphs">CELEBRATE, RESPECT &amp; VALUE</text>
    <text class="slate" x="46" y="633" font-size="37" textLength="757" lengthAdjust="spacingAndGlyphs">THE DIVERSITY OF AUSTRALIAN CULTURE.</text>
  </g>

  <g class="block-smile">
    <text class="orange" x="50" y="680" font-size="44" textLength="142" lengthAdjust="spacingAndGlyphs">SMILE</text>
    <text class="orange" x="196" y="661" font-size="18" textLength="250" lengthAdjust="spacingAndGlyphs">&amp; INFECT OTHERS WITH</text>
    <text class="orange" x="298" y="678" font-size="16" textLength="42" lengthAdjust="spacingAndGlyphs">YOUR</text>
    <text class="orange" x="50" y="712" font-size="30" textLength="396" lengthAdjust="spacingAndGlyphs">HAPPINESS &amp; HAVE FUN!</text>
  </g>

  <g class="block-right">
    <text class="ink" x="466" y="665" font-size="18" textLength="170" lengthAdjust="spacingAndGlyphs">ALWAYS DO THE</text>
    <text class="ink" x="642" y="684" font-size="50" textLength="158" lengthAdjust="spacingAndGlyphs">RIGHT</text>
    <text class="ink" x="468" y="709" font-size="52" textLength="154" lengthAdjust="spacingAndGlyphs">THING</text>
    <text class="ink" x="632" y="709" font-size="17" textLength="170" lengthAdjust="spacingAndGlyphs">WITHOUT EXCEPTION.</text>
  </g>

  <g class="block-unique">
    <text class="slate" x="48" y="742" font-size="18" textLength="180" lengthAdjust="spacingAndGlyphs">YOU ARE UNIQUE,</text>
    <text class="slate" x="73" y="760" font-size="18" textLength="157" lengthAdjust="spacingAndGlyphs">REVEL IN YOUR</text>
    <text class="slate" x="236" y="762" font-size="46" textLength="250" lengthAdjust="spacingAndGlyphs">INDIVIDUALITY.</text>
    <text class="orange" x="494" y="738" font-size="15" textLength="101" lengthAdjust="spacingAndGlyphs">ALWAYS BE</text>
    <text class="orange" x="494" y="758" font-size="18" textLength="104" lengthAdjust="spacingAndGlyphs">FOCUSED.</text>
    <text class="orange" x="604" y="762" font-size="46" textLength="198" lengthAdjust="spacingAndGlyphs">SOLUTION</text>
  </g>

  <text class="ink" x="46" y="806" font-size="42" textLength="757" lengthAdjust="spacingAndGlyphs">SEEK SUCCESS FIRSTLY FROM WITHIN.</text>

  <g class="block-lead">
    <text class="orange" x="47" y="836" font-size="18" textLength="375" lengthAdjust="spacingAndGlyphs">ONLY FOLLOW EXCEPTIONAL LEADERS.</text>
    <text class="ink" x="47" y="866" font-size="18" textLength="455" lengthAdjust="spacingAndGlyphs">IF THERE IS NO ONE LEFT TO FOLLOW, THEN LEAD!</text>
    <text class="slate" x="562" y="831" font-size="18" textLength="238" lengthAdjust="spacingAndGlyphs">ALWAYS LEAD WITH</text>
    <text class="slate" x="562" y="849" font-size="18" textLength="238" lengthAdjust="spacingAndGlyphs">PURPOSE, PASSION</text>
    <text class="slate" x="562" y="867" font-size="18" textLength="238" lengthAdjust="spacingAndGlyphs">&amp; COMMITMENT.</text>
  </g>

  <g class="block-practice">
    <text class="slate" x="46" y="890" font-size="18" textLength="433" lengthAdjust="spacingAndGlyphs">RESPOND TO COMPLEX SITUATIONS INNOVATIVELY,</text>
    <text class="slate" x="46" y="912" font-size="18" textLength="432" lengthAdjust="spacingAndGlyphs">CREATIVELY &amp; SAFELY WITHIN THE SCOPE OF</text>
    <text class="slate" x="488" y="915" font-size="38" textLength="314" lengthAdjust="spacingAndGlyphs">YOUR PRACTICE.</text>
  </g>

  <g class="block-can-do">
    <text class="orange" x="47" y="962" font-size="16" textLength="78" lengthAdjust="spacingAndGlyphs">ADOPT A</text>
    <text class="orange" x="133" y="962" font-size="50" textLength="217" lengthAdjust="spacingAndGlyphs">'CAN DO'</text>
    <text class="orange" x="47" y="983" font-size="22" textLength="302" lengthAdjust="spacingAndGlyphs">ATTITUDE TO EVERYTHING</text>
    <text class="orange" x="47" y="1005" font-size="22" textLength="274" lengthAdjust="spacingAndGlyphs">THAT COMES YOUR WAY.</text>
  </g>

  <g class="block-thoughts">
    <text class="ink" x="367" y="950" font-size="27" textLength="435" lengthAdjust="spacingAndGlyphs">CHOOSE YOUR THOUGHTS WISELY,</text>
    <text class="ink" x="367" y="982" font-size="30" textLength="433" lengthAdjust="spacingAndGlyphs">THEY CREATE YOUR REALITY.</text>
  </g>

  <text class="teal dream" x="330" y="1052" font-size="62" textLength="473" lengthAdjust="spacingAndGlyphs">LIVE YOUR DREAM.</text>

  <g class="brand">
    <rect class="brand-mark" x="90" y="1090" width="22" height="22"/>
    <text class="slate" x="122" y="1111" font-size="28" textLength="170" lengthAdjust="spacingAndGlyphs">CalmPeak</text>
  </g>
</svg>
</body>
</html>
```